Business card and promotional tool

I make a vacuum attachment kit that I will market as a business card/promotional tool. I need a one page brochure; the top half will be like a business card for a company, but also have space for an individual sales person to write in their name and phone number and a short "thank you" note. The bottom half would feature the product name and info and have several pictures. Attached is an example.

```html
<!DOCTYPE html>
<html lang="en">
<head>
<meta charset="utf-8">
<title>HoseMate Promo Card</title>
<link rel="stylesheet" href="https://fonts.googleapis.com/css2?family=Roboto:wght@400;500;700&family=Poppins:wght@400;600&display=swap">
<style>
:root{
  --red:#d9141c;
  --charcoal:#3d3438;
  --ink:#2f2a2d;
  --paper-top:#e9e9eb;
  --paper-gap:#f2f2f3;
  --paper-panel:#f4f4f5;
  --paper-strip:#e8e8e9;
  --rule:#3d3438;
  --white:#ffffff;
}
*{margin:0;padding:0;box-sizing:border-box}
html,body{width:1069px;height:1200px;overflow:hidden;background:var(--white)}
.flyer{position:relative;width:1069px;height:1200px;background:var(--paper-gap);font-family:"Roboto",sans-serif;color:var(--ink)}
.abs{position:absolute}

/* business card area */
.card{left:0;top:0;width:1069px;height:350px;background:var(--paper-top)}
.brand-name{font-family:"Roboto",sans-serif;font-weight:700;color:var(--ink);line-height:1}
.card .brand-name{left:72px;top:58px;font-size:56px;letter-spacing:-0.5px}
.rep-name{left:72px;top:148px;font-size:25px;font-weight:700;color:var(--red);letter-spacing:0.3px}
.rep-title{left:72px;top:177px;font-size:21px;color:#1f1b1d}
.contacts{left:72px;top:236px;list-style:none;font-family:"Poppins",sans-serif;font-size:17px;letter-spacing:1.2px;color:#1f1b1d}
.contacts li{display:flex;align-items:center;height:23.5px}
.contacts svg{width:17px;height:14px;margin-right:13px;fill:var(--red)}
.note-tab{left:536px;top:64px;width:463px;height:54px;background:var(--red);color:var(--white);font-weight:700;font-size:25px;display:flex;align-items:center;justify-content:center;letter-spacing:0.5px;box-shadow:0 8px 7px -4px rgba(0,0,0,.45)}
.note-line{left:536px;width:463px;height:2px;background:var(--rule)}

/* product area */
.quote-panel{left:0;top:371px;width:509px;height:464px;background:var(--charcoal)}
.quote-mark{left:56px;top:412px;width:80px;height:50px}
.quote-text{left:49px;top:474px;width:420px;color:var(--white);font-weight:700;font-size:37px;line-height:46.2px;letter-spacing:-0.2px}
.info-panel{left:509px;top:371px;width:509px;height:464px;background:var(--paper-panel)}
.info-panel .brand-name{left:45px;top:40px;font-size:70px;letter-spacing:-1px}
.accent-bar{left:1018px;top:371px;width:51px;height:464px;background:var(--red)}
.uses{left:43px;top:168px;list-style:none;font-family:"Poppins",sans-serif;font-size:31px;color:var(--ink)}
.uses li{display:flex;align-items:center;height:53.5px}
.uses svg{width:46px;height:38px;margin-right:25px;flex:none}

/* photo strip */
.strip{left:0;top:835px;width:1069px;height:292px;background:var(--paper-strip)}
.red-band{left:0;top:884px;width:1069px;height:20px;background:var(--red)}
.photo{top:928px;height:174px}
.photo-sink{left:0;width:335px;background:linear-gradient(135deg,#8a6a4a,#e9e6e4 50%,#6b4a30)}
.photo-lamp{left:365px;width:339px;background:linear-gradient(120deg,#5a3a22,#b88a58 45%,#3a2a22)}
.photo-car{left:733px;width:336px;background:linear-gradient(120deg,#9c7c58,#d8bc94 55%,#b49470)}

.footer{left:0;top:1127px;width:1069px;height:73px;background:var(--charcoal);color:var(--white);font-weight:700;font-size:35px;display:flex;align-items:center;justify-content:center;padding-left:22px}
</style>
</head>
<body>
<main class="flyer">
  <section class="abs card">
    <div class="abs brand-name">HoseMate</div>
    <div class="abs rep-name">JOHNATHAN DOE</div>
    <div class="abs rep-title">Director</div>
    <ul class="abs contacts">
      <li><svg viewBox="0 0 17 14"><path d="M1 5c0-3 15-3 15 0v2h-4V5H5v2H1z M4 8h9l2 6H2z"/></svg>012 345 6789</li>
      <li><svg viewBox="0 0 17 14"><path d="M1 1h15v12H1z" /><path d="M1 1l7.5 6L16 1" stroke="#e9e9eb" stroke-width="1.5" fill="none"/></svg>email@domain.com</li>
      <li><svg viewBox="0 0 17 14"><circle cx="8.5" cy="7" r="6.5"/><path d="M2 7h13M8.5 .5v13M4.5 2.5c2.5 2.5 2.5 6.5 0 9M12.5 2.5c-2.5 2.5-2.5 6.5 0 9" stroke="#e9e9eb" stroke-width="1" fill="none"/></svg>www.website.com</li>
    </ul>
    <div class="abs note-tab">NOTE</div>
    <div class="abs note-line" style="top:159px"></div>
    <div class="abs note-line" style="top:206px"></div>
    <div class="abs note-line" style="top:253px"></div>
    <div class="abs note-line" style="top:300px"></div>
  </section>

  <section class="abs quote-panel" aria-hidden="false"></section>
  <svg class="abs quote-mark" viewBox="0 0 80 50" aria-hidden="true">
    <path fill="#d9141c" d="M14 0h24L22 50H0zM54 0h26L62 50H40z"/>
  </svg>
  <p class="abs quote-text">HoseMate is your go anywhere, readh anything, nothing you can’t clean wet/dry vaccume attachment</p>

  <section class="abs info-panel">
    <div class="abs brand-name">HoseMate</div>
    <ul class="abs uses">
      <li><svg viewBox="0 0 46 38"><circle cx="19" cy="20" r="15" fill="none" stroke="#d9141c" stroke-width="4"/><path d="M11 19l7 8L41 4" fill="none" stroke="#2f2a2d" stroke-width="4.5" stroke-linecap="round" stroke-linejoin="round"/></svg>Plumbing Fixtures</li>
      <li><svg viewBox="0 0 46 38"><circle cx="19" cy="20" r="15" fill="none" stroke="#d9141c" stroke-width="4"/><path d="M11 19l7 8L41 4" fill="none" stroke="#2f2a2d" stroke-width="4.5" stroke-linecap="round" stroke-linejoin="round"/></svg>Refrigerator Coils</li>
      <li><svg viewBox="0 0 46 38"><circle cx="19" cy="20" r="15" fill="none" stroke="#d9141c" stroke-width="4"/><path d="M11 19l7 8L41 4" fill="none" stroke="#2f2a2d" stroke-width="4.5" stroke-linecap="round" stroke-linejoin="round"/></svg>Automative</li>
      <li><svg viewBox="0 0 46 38"><circle cx="19" cy="20" r="15" fill="none" stroke="#d9141c" stroke-width="4"/><path d="M11 19l7 8L41 4" fill="none" stroke="#2f2a2d" stroke-width="4.5" stroke-linecap="round" stroke-linejoin="round"/></svg>Dryer Vents</li>
      <li><svg viewBox="0 0 46 38"><circle cx="19" cy="20" r="15" fill="none" stroke="#d9141c" stroke-width="4"/><path d="M11 19l7 8L41 4" fill="none" stroke="#2f2a2d" stroke-width="4.5" stroke-linecap="round" stroke-linejoin="round"/></svg>And Much More!!</li>
    </ul>
  </section>
  <div class="abs accent-bar"></div>

  <section class="abs strip"></section>
  <div class="abs red-band"></div>
  <div class="abs photo photo-sink" role="img" aria-label="Photo of the attachment hose cleaning a bathroom sink drain on a granite counter"></div>
  <div class="abs photo photo-lamp" role="img" aria-label="Photo of a woman dusting a chandelier with the attachment"></div>
  <div class="abs photo photo-car" role="img" aria-label="Photo of the attachment cleaning between leather car seats"></div>

  <footer class="abs footer">www.hosemate-kit.com</footer>
</main>
</body>
</html>
```